Bodywork Hireline= take over industry

All services for bodywork hireline is FREE!! We need a flyer to show what our website offers for services. this is a flyer that needs to be universal for schools, employers, and CE providers. I need this flyer to look very professional and be able to tell the story of my website. Bodyworkhireline.com is a website that offer all these services for free

-post/search jobs (massage, aesthetics, front desk, and education)
-post/search CE Classes (Continuing education)
-post/search events (massage) like job fairs, paid chair events, volunteer events, and more
-post/search resumes
-post/search resumes
-Search license requirements in every state
-get latest news
-Ask questions about industry

Target Market(s)

Massage

Industry/Entity Type

Massage Therapy

Font styles to use
Serif

Requirements
Must have
• A great design must have everything my website offers. That all services are free on bodywork hireline.
• -post/search jobs (massage, aesthetics, front desk, and education)
• -post/search CE Classes (Continuing education)
• -post/search events (massage) like job fairs, paid chair events, volunteer events, and more...
• -post/search resumes
• -post/search resumes
• -Search license requirements in every state
• -get latest news
• -Ask questions about industry
• the color scheme of bodywork hireline logo

```html
<!DOCTYPE html>
<html lang="en">
<head>
<meta charset="utf-8">
<title>Bodywork Hireline Flyer</title>
<link href="https://fonts.googleapis.com/css2?family=Lora:wght@400;700&family=Open+Sans:wght@400;600&display=swap" rel="stylesheet">
<style>
  :root {
    --green-dark: #5f8f1e;
    --green: #8cc43c;
    --green-light: #d6ecb0;
    --green-pale: #eef7df;
    --green-border: #b9d98a;
    --text-dark: #2c3320;
    --text-body: #3a3a3a;
    --paper: #ffffff;
    --skin-warm: #c99a78;
  }
  * { box-sizing: border-box; margin: 0; padding: 0; }
  html, body { width: 851px; height: 1200px; overflow: hidden; background: var(--paper); }
  .flyer { position: relative; width: 851px; height: 1200px; background: var(--paper); overflow: hidden; font-family: "Open Sans", Arial, sans-serif; }

  .hero-photo {
    position: absolute; left: 0; top: 0; width: 851px; height: 540px;
    background: linear-gradient(100deg, #fbf8f3 0%, #f1e6da 28%, var(--skin-warm) 55%, #7a5a47 78%, #4a3a30 100%);
  }
  .hero-fade {
    position: absolute; left: 0; top: 0; width: 380px; height: 300px;
    background: linear-gradient(90deg, rgba(255,255,255,0.95) 60%, rgba(255,255,255,0) 100%);
  }

  .brand { position: absolute; left: 30px; top: 40px; width: 340px; }
  .brand-mark { width: 92px; height: 92px; border-radius: 50%; border: 5px solid var(--green); background: var(--paper); margin-left: 66px; }
  .brand-name { margin-top: 12px; font-family: "Lora", Georgia, serif; font-size: 24px; color: var(--green-dark); text-transform: uppercase; letter-spacing: 0.5px; white-space: nowrap; }
  .brand-url { margin-top: 2px; font-family: "Lora", Georgia, serif; font-size: 15px; color: var(--text-body); padding-left: 4px; }
  .brand-free { margin-top: 8px; font-family: "Lora", Georgia, serif; font-weight: 700; font-size: 16px; color: var(--green-dark); padding-left: 4px; }

  .wave { position: absolute; left: 0; top: 420px; width: 851px; height: 200px; }

  .services { position: absolute; left: 20px; top: 580px; width: 430px; list-style: none; }
  .service {
    display: flex; flex-direction: column; justify-content: center; align-items: center;
    height: 42px; margin-bottom: 10px; border-radius: 8px;
    background: linear-gradient(180deg, var(--green-pale) 0%, var(--green-light) 100%);
    border: 1px solid var(--green-border);
    color: var(--text-dark); font-size: 17px; line-height: 1.25; text-align: center;
  }
  .service.tall { height: 56px; }
  .service.taller { height: 66px; }
  .service small { font-size: 13px; color: var(--text-body); }

  .about {
    position: absolute; left: 462px; top: 560px; width: 400px; height: 400px; border-radius: 50%;
    background: var(--paper); border: 10px solid var(--green);
    box-shadow: 0 0 0 6px var(--green-light);
    padding: 66px 52px 0 46px;
  }
  .about-title { font-family: "Lora", Georgia, serif; font-weight: 700; font-size: 38px; color: var(--text-dark); text-align: center; margin-bottom: 10px; }
  .about-text { font-size: 13.5px; line-height: 1.4; color: var(--text-body); }

  .spa-still-life {
    position: absolute; left: 0; top: 1030px; width: 851px; height: 170px;
    background: linear-gradient(90deg, #e48fb3 0%, #c9d9a8 22%, #6d6458 40%, #f1ece2 58%, #f6f1d4 75%, #7fb048 100%);
  }
</style>
</head>
<body>
<div class="flyer">
  <div class="hero-photo" role="img" aria-label="Woman relaxing on a spa massage table beside candles and a folded towel"></div>
  <div class="hero-fade"></div>

  <div class="brand">
    <div class="brand-mark"></div>
    <div class="brand-name">Bodywork Hireline</div>
    <div class="brand-url">www.bodyworkhireline.com</div>
    <div class="brand-free">All services are FREE!</div>
  </div>

  <svg class="wave" viewBox="0 0 851 200" preserveAspectRatio="none" aria-hidden="true">
    <defs>
      <linearGradient id="waveGreen" x1="0" y1="0" x2="1" y2="0">
        <stop offset="0" stop-color="#8cc43c"/>
        <stop offset="1" stop-color="#c5e38e"/>
      </linearGradient>
    </defs>
    <path d="M0 60 C250 140 560 20 851 70 L851 200 L0 200 Z" fill="url(#waveGreen)"/>
    <path d="M0 105 C260 180 560 80 851 120 L851 200 L0 200 Z" fill="#ffffff"/>
  </svg>

  <ul class="services">
    <li class="service tall">Post/search jobs<small>(massage, aesthetics, front desk, and education)</small></li>
    <li class="service tall">Post/search CE Classes<small>(Continuing education)</small></li>
    <li class="service taller">Post/search events<small>(massage) like job fairs, paid chair events,<br>volunteer events &amp; more</small></li>
    <li class="service">Post/search resumes</li>
    <li class="service">Search license requirements in every state</li>
    <li class="service">Get latest news</li>
    <li class="service">Ask questions about industry</li>
  </ul>

  <div class="about">
    <h2 class="about-title">About Us</h2>
    <p class="about-text">We provide recruiting and job enhancement services for the massage therapy field and the spa industry. Employers can post job opportunities, browse resumes, and contact candidates of their choice. Massage therapists can take advantage of new job postings, stay up-to-date with the industry using our Continuing Education resources, and post resumes for maximum exposure.</p>
  </div>

  <div class="spa-still-life" role="img" aria-label="Spa still life of lotus flowers, stacked stones, rolled towels and white blossoms"></div>
</div>
</body>
</html>
```